Car Wrap Design for Parquet Company

We are a parquet retailer and parquet laying company from Germany. We need a car wrap design for our van. It should have a noticeable design and so be modern and look premium. Enclosed we present you three favorite designs from other companys. We especially like favorite1. We like the theme wood in the design. We'd like to hear the follwing in the advertisement: - Over 25 years experience (more that 25 years of experience) - Birch to Wenge (our slogan) quality - www.Dielen-Varnholt.de (our website) - 0624 - 73 15 829 (our telephone number) Our van is a Torvano K420 M3R3. Enclosed you find some pictures and the dimensions.
Colors
Designer to choose colors to be used in the design.
Look and feel
Each slider illustrates characteristics of the customer's brand and the style your logo design should communicate.

```html
<!DOCTYPE html>
<html lang="en">
<head>
<meta charset="utf-8">
<title>Dielen Varnholt – Van Wrap</title>
<link rel="stylesheet" href="https://fonts.googleapis.com/css2?family=Lato:wght@400;700&family=Lora:wght@400;700&display=swap">
<style>
  :root {
    --bg-left: #e7eef0;
    --bg-right: #fdfdfd;
    --frame: #3a3a3a;
    --wood-light: #cfab6e;
    --wood-mid: #bf9a5e;
    --wood-dark: #a8824b;
    --panel: #8a6d3b;
    --band: #2b170d;
    --glass: #f3f6f7;
    --white: #ffffff;
    --logo-orange: #d9590f;
    --logo-peach: #f9b277;
  }
  html, body {
    margin: 0;
    width: 1200px;
    height: 1200px;
    overflow: hidden;
  }
  .canvas {
    width: 1200px;
    height: 1200px;
    box-sizing: border-box;
    border: 1px solid var(--frame);
    background: linear-gradient(90deg, var(--bg-left), var(--bg-right));
  }
  .canvas svg { display: block; width: 100%; height: 100%; }
  .panel { fill: var(--panel); }
  .band { fill: var(--band); }
  .glass { fill: var(--glass); }
  .label-sans {
    font-family: "Lato", sans-serif;
    font-weight: 700;
    fill: var(--white);
  }
  .label-serif {
    font-family: "Lora", serif;
    fill: var(--white);
  }
  .brand-name {
    font-family: "Lato", sans-serif;
    font-weight: 700;
    fill: var(--logo-orange);
    letter-spacing: 4px;
  }
  .phone-icon {
    fill: none;
    stroke: var(--white);
    stroke-width: 7;
    stroke-linecap: round;
  }
</style>
</head>
<body>
<div class="canvas">
  <svg viewBox="0 0 1932 1932" xmlns="http://www.w3.org/2000/svg">
    <defs>
      <linearGradient id="wood" x1="0" y1="0" x2="0" y2="1">
        <stop offset="0" stop-color="var(--wood-mid)"/>
        <stop offset="0.5" stop-color="var(--wood-light)"/>
        <stop offset="1" stop-color="var(--wood-dark)"/>
      </linearGradient>
    </defs>

    <!-- Side view -->
    <g class="van-side">
      <path class="wood-skin" role="img" aria-label="Horizontal wooden plank texture covering the van body"
        fill="url(#wood)"
        d="M300 300 L1130 318 Q1230 340 1290 400 L1530 645 Q1640 680 1710 735 L1650 730 Q1638 748 1652 772 L1680 808 L1760 805 L1760 812 L225 805 L230 630 L240 620 L265 330 Q275 300 300 300 Z"/>
      <path class="glass" d="M1165 450 L1290 462 Q1330 470 1360 500 L1520 670 Q1535 697 1495 695 L1240 655 Q1190 648 1180 600 L1162 460 Z"/>
      <path class="band" d="M228 810 L1760 812 L1778 868 L1790 872 L1797 895 L1793 922 L1785 925 Q1770 940 1773 950 L1745 968 L1630 970 Q1635 820 1510 822 Q1400 830 1385 960 L638 943 Q635 818 515 815 Q410 815 390 938 L232 918 Q215 910 218 890 Q220 872 228 868 Z"/>

      <rect class="panel" x="272" y="425" width="381" height="205" rx="10"/>
      <text class="label-sans" x="288" y="478" font-size="50" font-weight="400" letter-spacing="3">Birch</text>
      <text class="label-sans" x="288" y="538" font-size="50" font-weight="400" letter-spacing="3">to Wenge</text>
      <text class="label-sans" x="288" y="614" font-size="68" letter-spacing="4">QUALITY</text>

      <rect class="panel" x="283" y="718" width="350" height="58" rx="10"/>
      <path class="phone-icon" d="M298 734 Q290 750 302 764"/>
      <text class="label-sans" x="318" y="764" font-size="40">0624 - 73 15 829</text>

      <rect fill="var(--white)" x="713" y="453" width="429" height="167" rx="10"/>
      <text class="brand-name" x="740" y="520" font-size="54">DIELEN</text>
      <text class="brand-name" x="740" y="585" font-size="54">VARNHOLT</text>

      <rect class="panel" x="733" y="710" width="747" height="85" rx="16"/>
      <text class="label-serif" x="746" y="770" font-size="44">More than <tspan font-size="62" font-weight="700">25 years</tspan> experience</text>

      <text class="label-sans" x="740" y="910" font-size="50" font-weight="400">www.Dielen-Varnholt.de</text>
    </g>

    <!-- Rear view -->
    <g class="van-rear">
      <path class="wood-skin" role="img" aria-label="Horizontal wooden plank texture covering the rear doors"
        fill="url(#wood)"
        d="M735 1138 L1135 1138 Q1165 1145 1172 1175 L1213 1460 L1183 1460 L1183 1640 L1180 1640 L1180 1672 L693 1672 L690 1640 L692 1460 L648 1460 L690 1190 Q705 1140 735 1138 Z"/>
      <rect class="glass" x="725" y="1555" width="190" height="75" rx="12"/>
      <rect class="glass" x="952" y="1559" width="80" height="12" rx="6"/>
      <path class="band" d="M648 1670 L1222 1670 L1222 1725 Q1220 1762 1200 1768 L1152 1764 Q1140 1750 1120 1750 L725 1750 L722 1762 L672 1768 Q650 1760 648 1735 Z"/>

      <rect fill="var(--logo-peach)" x="717" y="1211" width="428" height="170" rx="8"/>
      <text class="brand-name" x="745" y="1278" font-size="54">DIELEN</text>
      <text class="brand-name" x="745" y="1343" font-size="54">VARNHOLT</text>

      <rect class="panel" x="817" y="1362" width="350" height="58" rx="10"/>
      <path class="phone-icon" d="M832 1378 Q824 1394 836 1408"/>
      <text class="label-sans" x="852" y="1408" font-size="40">0624 - 73 15 829</text>

      <rect class="panel" x="707" y="1462" width="456" height="53" rx="10"/>
      <text class="label-sans" x="719" y="1500" font-size="31" letter-spacing="2">Birch to Wenge QUALITY</text>

      <text class="label-sans" x="728" y="1727" font-size="42" font-weight="400">www.Dielen-Varnholt.de</text>
    </g>
  </svg>
</div>
</body>
</html>
```